Photographer Card

I'm currently doing freelance photography and i need a creative design name card especially when i attend events.
I require a design that makes a STATEMENT.
Simple, elegant and nothing like the usual name cards ive seen around (Example: with a camera/tripod etc in the design).

Photographer: Dorian VP
Mobile: +65 84126957
E-mail: Dorian.VP.Photography@mailvista.net
Facebook: www.friendlane.net/dorian.vp.photography

Thanks for your time and hope it will turn out well! :)
Updates

Thanks for all your inputs!

Im liking the cursive feel.

Id prefer not to include the title "freelance"  :)

Also, im looking for a logo to establish myself

http://www.artmosaic.net/art/Cotton-Business-Card-583021746

Hi all! Thanks for the designs

"Capturing magical moments"
"Capturing magical moments that are gone forever"

Back design can be in big font "look HERE"

Maybe with focusing box 

Names can be played with horizontal and vertical.

Industry/Entity Type

Camera

Font styles to use
Script

```html
<!DOCTYPE html>
<html lang="en">
<head>
<meta charset="utf-8">
<title>Dorian VP Photography — Business Card</title>
<link rel="stylesheet" href="https://fonts.googleapis.com/css2?family=Josefin+Sans:wght@300&display=swap">
<style>
  :root {
    --card-orange: #f28a24;
    --frame-grey: #5f6266;
    --ink-grey: #5f6266;
  }
  * { margin: 0; padding: 0; box-sizing: border-box; }
  html, body {
    width: 1200px;
    height: 702px;
    overflow: hidden;
    background: var(--card-orange);
  }
  .card {
    position: relative;
    width: 1200px;
    height: 702px;
    background: var(--card-orange);
    font-family: "Josefin Sans", "Century Gothic", sans-serif;
    font-weight: 300;
    color: var(--ink-grey);
  }
  .card__frame {
    position: absolute;
    left: 0;
    top: 24px;
    width: 1200px;
    height: 656px;
    background: var(--frame-grey);
    border-radius: 78px;
  }
  .card__panel {
    position: absolute;
    left: 59px;
    top: 53px;
    width: 1083px;
    height: 590px;
    background: var(--card-orange);
  }
  .brand {
    position: absolute;
    left: 0;
    right: 0;
    top: 262px;
    text-align: center;
    font-size: 70px;
    line-height: 1;
    letter-spacing: -2px;
    white-space: nowrap;
  }
  .contact {
    position: absolute;
    left: 0;
    right: 0;
    text-align: center;
    font-size: 28px;
    line-height: 1;
    letter-spacing: -0.3px;
    white-space: nowrap;
  }
  .contact--primary { top: 563px; }
  .contact--social { top: 609px; }
</style>
</head>
<body>
  <main class="card">
    <div class="card__frame"></div>
    <div class="card__panel"></div>

    <h1 class="brand">DORIAN.VP</h1>

    <p class="contact contact--primary">| +65 84126957 | Dorian.VP.Photography@mailvista.net |</p>
    <p class="contact contact--social">| www.friendlane.net/dorian.vp.photography |</p>
  </main>
</body>
</html>
```